Web Design Business Card

I need a new business card designed, we recently rebranded and I need to get a fresh design to match our new logo, colours and branding.

Details:

Dorian Keeble | Founder & CEO
Address: 7 Fernhollow Lane, #04-09 Maplecrest Vale, Singapore 583104
Tel: +65 93468120
Web: www.plumtrove.com.sg
hello@plumtrove.com.sg

I've attached my old card as well

Requirements
Must have
• Front and Back
Interesting use of logo
Correct use of colour scheme

```html
<!DOCTYPE html>
<html lang="en">
<head>
<meta charset="utf-8">
<title>Plumtrove Business Card</title>
<link rel="stylesheet" href="https://fonts.googleapis.com/css2?family=Josefin+Sans:wght@400;600&family=Open+Sans:wght@400;600;700&display=swap">
<style>
  :root {
    --page: #e9ebe8;
    --card-white: #ffffff;
    --card-grey: #e4e5e6;
    --teal: #7fd3dc;
    --teal-deep: #4fc1d6;
    --ink: #2b2b2b;
    --logo-grey: #5b5b5b;
    --band-grey: #8f8f8f;
    --sky: #35b3e6;
    --sky-light: #7fd6f2;
    --frame: #b9aa95;
    --mark-pale: #9fe0ee;
    --word-pale: #8ea3aa;
    --tag-pale: #a8e4f2;
  }
  * { box-sizing: border-box; margin: 0; padding: 0; }
  html, body { width: 1200px; height: 1000px; overflow: hidden; }
  body {
    background: var(--page);
    font-family: "Open Sans", Arial, sans-serif;
    display: flex;
    flex-direction: column;
    align-items: center;
    justify-content: center;
    gap: 60px;
  }
  .card {
    position: relative;
    width: 700px;
    height: 400px;
    overflow: hidden;
    box-shadow: 0 10px 30px rgba(0,0,0,0.18);
  }

  /* Front */
  .card-front {
    background: radial-gradient(ellipse at 55% 45%, var(--card-white) 0%, var(--card-grey) 100%);
    border-radius: 34px 4px 34px 4px;
  }
  .person { position: absolute; left: 56px; top: 56px; }
  .person-name {
    font-family: "Josefin Sans", Arial, sans-serif;
    font-variant: small-caps;
    font-size: 40px;
    font-weight: 400;
    letter-spacing: 1px;
    color: var(--teal);
    line-height: 1;
  }
  .person-role {
    font-family: "Josefin Sans", Arial, sans-serif;
    font-variant: small-caps;
    font-size: 19px;
    color: var(--ink);
    margin-top: 6px;
    letter-spacing: 0.5px;
  }
  .brand {
    position: absolute;
    right: 50px;
    top: 118px;
    display: flex;
    align-items: center;
    gap: 12px;
  }
  .brand-dot { width: 50px; height: 50px; border-radius: 50%; background: var(--teal-deep); }
  .brand-name { font-size: 42px; font-weight: 700; color: var(--logo-grey); letter-spacing: -0.5px; }
  .contacts {
    position: absolute;
    left: 330px;
    top: 200px;
    list-style: none;
  }
  .contacts li {
    display: flex;
    align-items: center;
    gap: 14px;
    font-size: 17px;
    color: var(--ink);
    height: 28px;
  }
  .contacts svg { width: 18px; height: 18px; }
  .rule-set { position: absolute; left: 0; right: 0; top: 302px; height: 12px; }
  .rule-line { position: absolute; left: 0; right: 0; top: 8px; height: 3px; background: var(--teal); }
  .rule-band { position: absolute; top: 0; height: 5px; }
  .rule-band.grey { left: 140px; width: 240px; background: var(--band-grey); }
  .rule-band.teal { left: 380px; width: 220px; background: var(--teal); }
  .address {
    position: absolute;
    left: 34px;
    bottom: 34px;
    display: flex;
    align-items: center;
    gap: 10px;
    font-size: 19px;
    color: var(--ink);
  }
  .address svg { width: 20px; height: 20px; }

  /* Back */
  .card-back {
    border-radius: 4px 4px 34px 4px;
    background: var(--frame);
    padding: 12px;
  }
  .back-field {
    width: 100%;
    height: 100%;
    border-radius: 2px 2px 26px 2px;
    background: radial-gradient(ellipse at 45% 55%, var(--sky-light) 0%, var(--sky) 75%);
    position: relative;
  }
  .back-brand {
    position: absolute;
    left: 56px;
    top: 113px;
    display: flex;
    align-items: center;
    gap: 14px;
  }
  .back-dot { width: 150px; height: 150px; border-radius: 50%; background: var(--mark-pale); opacity: 0.8; flex: none; }
  .back-text { display: flex; flex-direction: column; }
  .back-word { font-size: 72px; font-weight: 700; color: var(--word-pale); letter-spacing: -1px; line-height: 1; }
  .back-tagline {
    margin-top: 6px;
    font-size: 20px;
    font-weight: 600;
    letter-spacing: 2px;
    color: var(--tag-pale);
    white-space: nowrap;
  }
</style>
</head>
<body>
  <section class="card card-front">
    <div class="person">
      <h1 class="person-name">Dorian Keeble</h1>
      <p class="person-role">Founder &amp; CEO</p>
    </div>
    <div class="brand">
      <span class="brand-dot"></span>
      <span class="brand-name">plumtrove</span>
    </div>
    <ul class="contacts">
      <li>
        <svg viewBox="0 0 18 18"><rect x="4" y="1.5" width="10" height="15" rx="2" fill="none" stroke="#2b2b2b" stroke-width="1.6"/><line x1="7" y1="14" x2="11" y2="14" stroke="#2b2b2b" stroke-width="1.4"/></svg>
        +65 93468120
      </li>
      <li>
        <svg viewBox="0 0 18 18"><text x="9" y="14" text-anchor="middle" font-family="Open Sans, sans-serif" font-size="16" font-weight="700" fill="#2b2b2b">@</text></svg>
        hello@plumtrove.com.sg
      </li>
      <li>
        <svg viewBox="0 0 18 18" fill="none" stroke="#2b2b2b" stroke-width="1.4"><circle cx="9" cy="9" r="7.5"/><ellipse cx="9" cy="9" rx="3.2" ry="7.5"/><line x1="1.5" y1="9" x2="16.5" y2="9"/></svg>
        www.plumtrove.com.sg
      </li>
    </ul>
    <div class="rule-set">
      <div class="rule-line"></div>
      <div class="rule-band grey"></div>
      <div class="rule-band teal"></div>
    </div>
    <p class="address">
      <svg viewBox="0 0 20 20"><path d="M10 1.5a6 6 0 0 0-6 6c0 4.5 6 11 6 11s6-6.5 6-11a6 6 0 0 0-6-6z" fill="none" stroke="#2b2b2b" stroke-width="1.6"/><circle cx="10" cy="7.5" r="2.2" fill="#2b2b2b"/></svg>
      7 Fernhollow Lane, #04-09 Maplecrest Vale, Singapore 583104
    </p>
  </section>

  <section class="card card-back">
    <div class="back-field">
      <div class="back-brand">
        <span class="back-dot"></span>
        <div class="back-text">
          <span class="back-word">plumtrove</span>
          <p class="back-tagline">WEB DESIGN &amp; CONSULTING</p>
        </div>
      </div>
    </div>
  </section>
</body>
</html>
```